The Corvanta Group's website for high impact furniture promotions

I am looking for a simple website. we are a promotional company that runs events for furniture stores to increase sales for short periods of time. i would like the website to have about 4 areas to explain our company. I would like it to be simple and user friendly. I would like a link to chatterbook and a contact section. I am attaching our logo that i would like somewhere large or possibly in the backround. I am open to different color schemes. I would like to convey fast paced, modern, reliable. I am open to all different styles and look forward to seeing whats out there. we are looking for a quick turn around, so if we see one that we like quick, we will pick that one thanks
Updates
Project Deadline Extended
Reason: looking for some really creative designs and want to give a fair amount of time to produce
Target Market(s)
Retail Furniture store owners
Industry/Entity Type
It Company
Number of Pages Required
1 page
Colors
Designer to choose colors to be used in the design.
Look and feel
Each slider illustrates characteristics of the customer's brand and the style your logo design should communicate.

```html
<!DOCTYPE html>
<html lang="en">
<head>
<meta charset="utf-8">
<title>The Corvanta Group — High Impact Furniture Promotions</title>
<link href="https://fonts.googleapis.com/css2?family=Playfair+Display:wght@400;700&family=Open+Sans:wght@400;600;700&display=swap" rel="stylesheet">
<style>
:root{
  --navy:#1c2341;
  --navy-deep:#141a33;
  --bronze:#8d6a3e;
  --bronze-light:#b08650;
  --ink:#2a2a2a;
  --muted:#8a8a8a;
  --paper:#ffffff;
  --mist:#f3f3f3;
  --gallery:#2b2624;
  --line:#e4e4e4;
}
*{box-sizing:border-box;margin:0;padding:0}
html,body{width:730px;height:1200px;overflow:hidden;background:var(--paper)}
body{font-family:"Open Sans",Arial,sans-serif;color:var(--ink);position:relative}
.serif{font-family:"Playfair Display",Georgia,serif}

/* header */
.site-header{position:absolute;top:0;left:0;width:730px;height:68px;background:var(--paper);border-bottom:1px solid var(--line)}
.brand{position:absolute;left:70px;top:10px;display:flex;flex-direction:column;align-items:center;width:60px}
.brand-dot{width:28px;height:28px;border-radius:50%;background:var(--bronze)}
.brand-name{margin-top:4px;font-family:"Playfair Display",Georgia,serif;font-size:7px;letter-spacing:1px;color:var(--bronze);text-align:center;line-height:1.15;text-transform:uppercase}
.main-nav{position:absolute;right:110px;top:28px;display:flex;gap:22px;font-size:9px;color:#555}
.search-btn{position:absolute;right:80px;top:25px;width:16px;height:16px;border:1px solid #bbb;border-radius:50%}

/* hero */
.hero{position:absolute;top:68px;left:0;width:730px;height:194px;background:linear-gradient(100deg,var(--navy-deep),var(--navy) 60%,#262f55)}
.hero-title{position:absolute;left:80px;top:38px;color:#fff;font-size:26px;font-weight:700;line-height:1.15}
.hero-sub{position:absolute;left:80px;top:104px;color:#c8cbe0;font-size:8px}
.btn{display:inline-block;background:var(--bronze);color:#fff;font-size:7px;font-weight:700;letter-spacing:1px;text-transform:uppercase;padding:7px 14px;border-radius:12px}
.hero .btn{position:absolute;left:80px;top:134px}
.hero-photo{position:absolute;left:320px;top:18px;width:300px;height:160px;border-radius:4px;background:radial-gradient(ellipse at 55% 60%,#2f4aa0 0%,#243674 35%,rgba(28,35,65,0) 70%)}

/* about */
.about{position:absolute;top:262px;left:0;width:730px;height:286px;background:var(--mist)}
.eyebrow{font-size:6px;letter-spacing:1px;color:var(--bronze);text-transform:uppercase;font-weight:600}
.about .eyebrow{position:absolute;left:80px;top:46px}
.about-title{position:absolute;left:80px;top:60px;width:300px;font-size:13px;font-weight:700;line-height:1.3}
.about-copy{position:absolute;left:80px;top:110px;width:300px;font-size:6.5px;line-height:1.6;color:var(--muted)}
.about-copy p+p{margin-top:8px}
.about .btn{position:absolute;left:80px;top:232px}
.services{position:absolute;left:435px;top:40px;display:grid;grid-template-columns:105px 105px;gap:12px}
.service-card{background:#fff;height:90px;padding:10px;box-shadow:0 3px 10px rgba(0,0,0,.08)}
.service-card h3{font-family:"Playfair Display",Georgia,serif;font-size:8px;margin-bottom:6px}
.service-card p{font-size:5.5px;line-height:1.6;color:var(--muted)}
.service-card span{display:block;margin-top:8px;font-size:5.5px;color:var(--bronze)}

/* product heading */
.product-head{position:absolute;top:548px;left:0;width:730px;height:142px;text-align:center}
.product-head .eyebrow{margin-top:48px}
.product-head h2{font-size:32px;font-weight:700;margin-top:6px}

/* gallery */
.gallery{position:absolute;top:690px;left:0;width:730px;height:415px;background:var(--gallery)}
.tile{position:absolute;overflow:hidden}
.tile .tag{position:absolute;left:10px;top:12px;background:var(--bronze);color:#fff;font-size:7px;font-weight:700;padding:4px 10px}
.tile .shop{position:absolute;left:50%;bottom:14px;transform:translateX(-50%);border:1px solid #fff;color:#fff;font-size:6px;letter-spacing:1px;padding:5px 12px;background:rgba(0,0,0,.35);text-transform:uppercase}
.t-big{left:45px;top:20px;width:310px;height:375px;background:linear-gradient(160deg,#d9cbb4,#b79a72 55%,#6f5438)}
.t1{left:365px;top:20px;width:155px;height:180px;background:linear-gradient(170deg,#e9e6e1,#b7aea3 60%,#5b4e44)}
.t2{left:530px;top:20px;width:155px;height:180px;background:linear-gradient(170deg,#d8d5d0,#8c8580 60%,#3e3835)}
.t3{left:365px;top:210px;width:155px;height:185px;background:linear-gradient(170deg,#cfc7bc,#8f7c6a 55%,#3d322b)}
.t4{left:530px;top:210px;width:155px;height:185px;background:linear-gradient(170deg,#d9d6d2,#7a746f 55%,#211d1b)}

/* footer */
.site-footer{position:absolute;top:1105px;left:0;width:730px;height:95px;background:var(--bronze);color:#fff}
.f-col{position:absolute;top:18px;display:flex;gap:8px}
.f-icon{width:22px;height:22px;border-radius:50%;border:1px solid rgba(255,255,255,.7);display:flex;align-items:center;justify-content:center}
.f-col h4{font-size:7px;font-weight:700;text-transform:uppercase;letter-spacing:.5px}
.f-col p{font-size:6px;line-height:1.5;opacity:.85;margin-top:2px}
.socials{display:flex;gap:8px;margin-top:8px}
.socials span{width:16px;height:16px;border-radius:50%;border:1px solid rgba(255,255,255,.7)}
.footer-bar{position:absolute;left:80px;right:80px;bottom:10px;border-top:1px solid rgba(255,255,255,.3);padding-top:7px;display:flex;gap:26px;font-size:6px;opacity:.85}
</style>
</head>
<body>

<header class="site-header">
  <div class="brand"><div class="brand-dot"></div><div class="brand-name">The Corvanta<br>Group</div></div>
  <nav class="main-nav"><span>Home</span><span>About Us</span><span>Services</span><span>Contact</span></nav>
  <div class="search-btn"></div>
</header>

<section class="hero">
  <h1 class="hero-title serif">High impact<br>Furniture promotions</h1>
  <p class="hero-sub">Events that move furniture in short windows</p>
  <span class="btn">Check more</span>
  <div class="hero-photo" role="img" aria-label="Blue tufted velvet sofa in a dark room"></div>
</section>

<section class="about">
  <p class="eyebrow">Promotions that make a difference in stores</p>
  <h2 class="about-title serif">Lorem ipsum dolor sit amet, consectetur adipiscing elit. Pellentesque accumsan.</h2>
  <div class="about-copy">
    <p>We plan and run short sales events for furniture stores. Our team handles the marketing, staffing and floor setup so owners can focus on closing deals and moving stock quickly.</p>
    <p>Every event is built around your store, your inventory and your goals. We track results daily and adjust fast, giving you a reliable lift in traffic and revenue when you need it most.</p>
  </div>
  <span class="btn">Read more</span>
  <div class="services">
    <div class="service-card"><h3>Services 1</h3><p>Event planning tailored to your showroom and stock levels.</p><span>Learn more</span></div>
    <div class="service-card"><h3>Services 2</h3><p>Targeted advertising that brings buyers through the door.</p><span>Learn more</span></div>
    <div class="service-card"><h3>Services 3</h3><p>Trained sales staff on the floor for every event day.</p><span>Learn more</span></div>
    <div class="service-card"><h3>Services 4</h3><p>Clear daily reports on traffic, sales and results.</p><span>Learn more</span></div>
  </div>
</section>

<section class="product-head">
  <p class="eyebrow">Promotions that make a difference in stores</p>
  <h2 class="serif">Our product</h2>
</section>

<section class="gallery">
  <div class="tile t-big" role="img" aria-label="Round wooden dining table with chairs in a bright room"><span class="tag">25% OFF</span><span class="shop">Shop now</span></div>
  <div class="tile t1" role="img" aria-label="White dining chairs around a table"><span class="tag">25% OFF</span><span class="shop">Shop now</span></div>
  <div class="tile t2" role="img" aria-label="Grey sofa with cushions in a living room"><span class="tag">25% OFF</span><span class="shop">Shop now</span></div>
  <div class="tile t3" role="img" aria-label="Patterned armchair and side table"><span class="tag">25% OFF</span><span class="shop">Shop now</span></div>
  <div class="tile t4" role="img" aria-label="Dark sideboard cabinet with decor"><span class="tag">25% OFF</span><span class="shop">Shop now</span></div>
</section>

<footer class="site-footer">
  <div class="f-col" style="left:80px">
    <div class="f-icon"><svg width="10" height="12" viewBox="0 0 10 12"><path d="M5 0a4 4 0 0 0-4 4c0 3 4 8 4 8s4-5 4-8a4 4 0 0 0-4-4zm0 5.5A1.5 1.5 0 1 1 5 2.5a1.5 1.5 0 0 1 0 3z" fill="#fff"/></svg></div>
    <div><h4>Our location</h4><p>214 Harlow Street, Suite 9<br>Brookfield, OH 44012</p></div>
  </div>
  <div class="f-col" style="left:270px">
    <div class="f-icon"><svg width="11" height="11" viewBox="0 0 11 11"><path d="M2.2 0.5l1.8 2.3-1 1.2c.7 1.5 1.9 2.7 3.4 3.4l1.2-1 2.3 1.8-.8 1.8C5 9.8 1.2 6 .4 1.3z" fill="#fff"/></svg></div>
    <div><h4>Call us now</h4><p>(555) 013-4728<br>hello@corvantagroup.com</p></div>
  </div>
  <div class="f-col" style="left:460px;display:block">
    <h4>Stay connected with us</h4>
    <div class="socials" aria-label="chatterbook and other social links"><span></span><span></span><span></span><span></span><span></span></div>
  </div>
  <div class="footer-bar"><span>Home</span><span>About Us</span><span>Services</span><span>Contact</span><span>© The Corvanta Group</span></div>
</footer>

</body>
</html>
```